Vale Crest Motors Business Card

Would like a cutting edge / high end Automotive Business card design. Please see current card which is old and dated. Would like to maintain the Vale Crest Motors logo and same information (address, website, etc).

See our website for the look and feel of what we offer - www.valecrestmotors.example

Target Market(s)

Upper class car buyers

Contact Information for Business Card

Modern high end business card design

Requirements
Nice to have
• Carbon Fiber look background

```html
<!DOCTYPE html>
<html lang="en">
<head>
<meta charset="utf-8">
<title>Vale Crest Motors Business Card</title>
<link rel="stylesheet" href="https://fonts.googleapis.com/css2?family=Montserrat:wght@300;400;700&family=Alex+Brush&display=swap">
<style>
  :root {
    --stage: #c49a3c;
    --card-dark: #070707;
    --gold: #e1b95a;
    --white: #ffffff;
    --soft-white: #e6e6e6;
    --divider: #6d5a2f;
  }
  * { margin: 0; padding: 0; box-sizing: border-box; }
  html, body { width: 1122px; height: 1200px; overflow: hidden; }
  body { background: var(--stage); font-family: "Montserrat", sans-serif; position: relative; }

  .card {
    position: absolute;
    left: 133px;
    width: 861px;
    height: 492px;
    background: var(--card-dark);
    overflow: hidden;
    box-shadow: 0 1px 3px rgba(0,0,0,0.45);
  }
  .card--front { top: 71px; }
  .card--back { top: 618px; }

  .card__texture {
    position: absolute; inset: 0;
    background:
      radial-gradient(ellipse 40% 35% at 0% 0%, rgba(150,100,40,0.35), transparent 70%),
      radial-gradient(ellipse 35% 30% at 100% 100%, rgba(190,50,25,0.55), transparent 70%),
      radial-gradient(ellipse 45% 40% at 0% 100%, rgba(80,80,80,0.35), transparent 70%),
      radial-gradient(ellipse 40% 35% at 80% 0%, rgba(70,70,70,0.3), transparent 70%),
      linear-gradient(135deg, #1a1a1a 0%, #050505 45%, #0c0c0c 100%);
  }

  .wordmark {
    position: absolute; left: 0; right: 0;
    text-align: center;
    font-weight: 700;
    font-size: 50px;
    letter-spacing: 0.5px;
  }
  .card--front .wordmark { top: 112px; color: var(--gold); }
  .card--back .wordmark { top: 190px; color: var(--white); font-size: 44px; }

  .address {
    position: absolute; left: 0; width: 832px; top: 254px;
    text-align: center;
    color: var(--white);
    font-size: 18px;
    line-height: 22px;
  }

  .person {
    position: absolute; right: 479px; top: 336px;
    text-align: right;
  }
  .person__name { color: var(--gold); font-weight: 700; font-size: 45px; line-height: 52px; white-space: nowrap; }
  .person__role { color: var(--white); font-weight: 300; font-size: 26px; line-height: 34px; margin-top: 6px; }

  .divider {
    position: absolute; left: 411px; top: 346px;
    width: 1px; height: 78px;
    background: var(--divider);
  }

  .contacts { position: absolute; left: 440px; top: 338px; list-style: none; }
  .contacts__item {
    display: flex; align-items: center;
    height: 23px;
    color: var(--soft-white);
    font-weight: 300;
    font-size: 19px;
    white-space: nowrap;
  }
  .contacts__icon { width: 16px; height: 16px; margin-right: 18px; fill: var(--gold); flex: none; }

  .tagline {
    position: absolute; left: 0; right: 0; top: 288px;
    text-align: center;
    font-family: "Alex Brush", cursive;
    color: var(--white);
    font-size: 27px;
  }
  .values {
    position: absolute; left: 330px; top: 334px;
    width: 194px; height: 18px;
    background: var(--white);
    color: #111;
    font-size: 14px;
    line-height: 18px;
    text-align: center;
    white-space: nowrap;
  }
</style>
</head>
<body>
  <section class="card card--front">
    <div class="card__texture" role="img" aria-label="Dark carbon fiber weave texture with warm gold and red glints"></div>
    <div class="wordmark">Vale Crest Motors</div>
    <p class="address">1840 Harbor Ridge Rd #B<br>Ashford, CA 95012</p>
    <div class="person">
      <div class="person__name">Daniel Rowe</div>
      <div class="person__role">Owner</div>
    </div>
    <div class="divider"></div>
    <ul class="contacts">
      <li class="contacts__item">
        <svg class="contacts__icon" viewBox="0 0 24 24"><path d="M6.6 10.8a15 15 0 0 0 6.6 6.6l2.2-2.2c.3-.3.7-.4 1-.2 1.1.4 2.3.6 3.6.6.6 0 1 .4 1 1V20c0 .6-.4 1-1 1C10.6 21 3 13.4 3 4c0-.6.4-1 1-1h3.5c.6 0 1 .4 1 1 0 1.3.2 2.5.6 3.6.1.3 0 .7-.2 1z"/></svg>
        415 555 0187
      </li>
      <li class="contacts__item">
        <svg class="contacts__icon" viewBox="0 0 24 24"><path d="M7 3h9v5H7zM3 9h18v12H3zm4 3v2h2v-2zm4 0v2h2v-2zm4 0v2h2v-2zm-8 4v2h2v-2zm4 0v2h2v-2zm4 0v2h2v-2z"/></svg>
        415 555 0142
      </li>
      <li class="contacts__item">
        <svg class="contacts__icon" viewBox="0 0 24 24"><path d="M12 2a10 10 0 1 0 5 18.7l-1-1.7A8 8 0 1 1 20 12v1.5a1.5 1.5 0 0 1-3 0V12a5 5 0 1 0-1.5 3.6A3.5 3.5 0 0 0 22 13.5V12A10 10 0 0 0 12 2zm0 13a3 3 0 1 1 0-6 3 3 0 0 1 0 6z"/></svg>
        daniel@valecrestmotors.example
      </li>
      <li class="contacts__item">
        <svg class="contacts__icon" viewBox="0 0 24 24"><path d="M12 2a10 10 0 1 0 0 20 10 10 0 0 0 0-20zm6.9 6h-3a15 15 0 0 0-1.3-3.9A8 8 0 0 1 18.9 8zM12 4c.8 1.2 1.5 2.5 1.9 4h-3.8c.4-1.5 1.1-2.8 1.9-4zM4.3 14a8 8 0 0 1 0-4h3.4a16 16 0 0 0 0 4zm.8 2h3a15 15 0 0 0 1.3 3.9A8 8 0 0 1 5.1 16zm3-8h-3a8 8 0 0 1 4.3-3.9A15 15 0 0 0 8.1 8zM12 20c-.8-1.2-1.5-2.5-1.9-4h3.8c-.4 1.5-1.1 2.8-1.9 4zm2.3-6H9.7a14 14 0 0 1 0-4h4.6a14 14 0 0 1 0 4zm.3 5.9a15 15 0 0 0 1.3-3.9h3a8 8 0 0 1-4.3 3.9zm1.7-5.9a16 16 0 0 0 0-4h3.4a8 8 0 0 1 0 4z"/></svg>
        www.valecrestmotors.example
      </li>
    </ul>
  </section>

  <section class="card card--back">
    <div class="card__texture" role="img" aria-label="Dark carbon fiber weave texture with warm gold and red glints"></div>
    <div class="wordmark">Vale Crest Motors</div>
    <p class="tagline">Offering the Finest in Luxury &amp; Exotic Sport Cars</p>
    <div class="values">Quality | Integrity |Service</div>
  </section>
</body>
</html>
```